Fun, Clean Business Card For Family Focused Travel Agency

I need a business card using specific colors and fonts as in the uploaded files. Ideally, I would like a large image of the logo on the back and all the contact info on the front. Maybe the stars/dots somewhere in a flowy form.

I do want it the contact information to be clear and easy to read. I don't want it to look too busy. Maybe even a bit minimalist.

I plan or ordering the ROUNDED CORNER business cards from Cardwell Press, so please consider that in your design.

Target Market(s)

Families with children, couples, groups of friends

Contact Information for Business Card

Marla Quent, Owner
Marla@TidewayTrips.example
Cell Phone Number 555-218-6034
Office Phone Number 555-647-1295
Specializing in Fablecrest destinations, Goldmere Parkside Resort, Cruises and All-Inclusive Vacations.

Nice but not required:
www.TidewayTrips.example
Facebook, Instagram, Twitter icons with username: TidewayTrips

Font styles to use
Sans Serif

Requirements
Must have
• Please try to use the colors from the logo as much as possible. I understand lighter shades/colors may be needed for some things.
Should not have
• NO SERIF FONTS. That is really the only thing I do not want at all

```html
<!DOCTYPE html>
<html lang="en">
<head>
<meta charset="utf-8">
<title>Tideway Trips – Business Card</title>
<link href="https://fonts.googleapis.com/css2?family=Fira+Sans:wght@400;500;600;700&family=Kaushan+Script&display=swap" rel="stylesheet">
<style>
  :root{
    --navy:#0f1a4a;
    --sky:#3aa6d6;
    --teal:#12b39a;
    --orange:#f07f1e;
    --lime:#9cc31b;
    --gold:#e2b323;
    --rule:#bdbdbd;
    --guide:#e3e3e3;
    --ink:#111;
  }
  html,body{margin:0;padding:0;}
  body{width:1200px;height:1000px;overflow:hidden;background:#fff;font-family:"Fira Sans",Arial,sans-serif;position:relative;}
  .sheet-guides{position:absolute;left:0;top:0;}
  .dim-label{position:absolute;font-size:13px;color:#333;font-family:Arial,Helvetica,sans-serif;}
  .side-label{position:absolute;font-family:Arial,Helvetica,sans-serif;font-weight:700;font-size:27px;letter-spacing:1px;color:var(--ink);}
  .brief-note{position:absolute;left:32px;top:792px;font-family:Arial,Helvetica,sans-serif;font-size:26px;line-height:35px;color:var(--ink);}
  .card{position:absolute;left:289px;width:668px;height:407px;border:1px solid var(--rule);border-radius:40px;overflow:hidden;background:#fff;box-sizing:border-box;}
  .card-front{top:60px;}
  .card-back{top:570px;}
  .confetti{position:absolute;left:0;width:100%;}
  .confetti-top{top:0;height:95px;background:linear-gradient(90deg,rgba(18,179,154,.16),rgba(226,179,35,.16),rgba(58,166,214,.14),rgba(240,127,30,.14),rgba(156,195,27,.16));
    -webkit-mask:linear-gradient(180deg,#000 40%,transparent);mask:linear-gradient(180deg,#000 40%,transparent);}
  .confetti-bottom{bottom:0;height:90px;background:linear-gradient(90deg,rgba(240,127,30,.14),rgba(58,166,214,.16),rgba(156,195,27,.16),rgba(226,179,35,.14),rgba(18,179,154,.16));
    -webkit-mask:linear-gradient(0deg,#000 40%,transparent);mask:linear-gradient(0deg,#000 40%,transparent);}
  .contact{position:absolute;left:0;width:100%;text-align:center;color:var(--navy);}
  .name{top:70px;font-size:32px;font-weight:700;letter-spacing:.5px;}
  .name .role{font-size:23px;font-weight:400;color:var(--sky);letter-spacing:0;}
  .email{top:117px;font-size:23px;display:flex;justify-content:center;align-items:center;gap:8px;}
  .phones{top:157px;font-size:26px;font-weight:700;display:flex;justify-content:center;align-items:center;gap:30px;}
  .phones span{display:inline-flex;align-items:center;gap:7px;}
  .special-head{top:196px;font-family:"Kaushan Script",cursive;font-size:18px;color:var(--sky);}
  .special-list{top:228px;font-size:16px;line-height:23px;font-weight:500;}
  .socials{top:289px;font-size:16px;font-weight:600;display:flex;justify-content:center;gap:22px;}
  .socials span{display:inline-flex;align-items:center;gap:6px;}
  .socials i{display:inline-block;width:15px;height:15px;border-radius:3px;}
  .web{top:322px;font-size:14px;font-weight:700;letter-spacing:1.6px;}
  .brand{position:absolute;left:0;top:0;width:100%;height:100%;display:flex;align-items:center;justify-content:center;gap:22px;}
  .brand-dot{width:78px;height:78px;border-radius:50%;background:var(--teal);}
  .brand-name{font-size:66px;font-weight:700;color:var(--navy);}
</style>
</head>
<body>

<svg class="sheet-guides" width="1200" height="1000" viewBox="0 0 1200 1000">
  <g fill="none" stroke="var(--guide)" stroke-width="2">
    <line x1="312" y1="40" x2="932" y2="40"/>
    <line x1="968" y1="62" x2="968" y2="467"/>
    <line x1="312" y1="550" x2="932" y2="550"/>
    <line x1="968" y1="572" x2="968" y2="977"/>
  </g>
  <g fill="var(--guide)">
    <polygon points="306,40 320,33 320,47"/><polygon points="938,40 924,33 924,47"/>
    <polygon points="968,55 961,69 975,69"/><polygon points="968,474 961,460 975,460"/>
    <polygon points="306,550 320,543 320,557"/><polygon points="938,550 924,543 924,557"/>
    <polygon points="968,565 961,579 975,579"/><polygon points="968,984 961,970 975,970"/>
  </g>
</svg>

<div class="dim-label" style="left:601px;top:14px;">90mm</div>
<div class="dim-label" style="left:987px;top:269px;">55mm</div>
<div class="dim-label" style="left:601px;top:525px;">90mm</div>
<div class="dim-label" style="left:987px;top:770px;">55mm</div>

<div class="side-label" style="left:165px;top:90px;">FRONT</div>
<div class="side-label" style="left:187px;top:608px;">BACK</div>

<div class="brief-note">Fun, Clean<br>Business Card<br>For Family<br>Focused<br>Travel Agency</div>

<section class="card card-front">
  <div class="confetti confetti-top" role="img" aria-label="Scattered colourful stars and dots along the top edge"></div>
  <div class="confetti confetti-bottom" role="img" aria-label="Scattered colourful stars and dots along the bottom edge"></div>

  <div class="contact name">MARLA QUENT<span class="role"> ,owner</span></div>
  <div class="contact email">
    <svg width="26" height="18" viewBox="0 0 26 18"><rect width="26" height="18" rx="2" fill="var(--lime)"/><path d="M1 2 L13 11 L25 2" fill="none" stroke="#fff" stroke-width="2"/></svg>
    Marla@TidewayTrips.example
  </div>
  <div class="contact phones">
    <span><svg width="14" height="24" viewBox="0 0 14 24"><rect x="1" y="1" width="12" height="22" rx="2.5" fill="none" stroke="var(--orange)" stroke-width="2"/><rect x="3.5" y="4" width="7" height="13" fill="var(--orange)"/><circle cx="7" cy="20" r="1.2" fill="var(--orange)"/></svg>555-218-6034</span>
    <span><svg width="20" height="22" viewBox="0 0 20 22"><path d="M4 1 L8 5 L6 8 Q8 13 12 16 L15 14 L19 18 L16 21 Q9 21 4 15 Q0 9 1 4 Z" fill="var(--teal)"/></svg>555-647-1295</span>
  </div>
  <div class="contact special-head">Specializing in</div>
  <div class="contact special-list">Fablecrest destinations, Goldmere Parkside Resort,<br>Cruises and All-Inclusive Vacations</div>
  <div class="contact socials">
    <span><i style="background:var(--teal)"></i>TidewayTrips</span>
    <span><i style="background:var(--sky)"></i>TidewayTrips</span>
    <span><i style="background:var(--orange)"></i>TidewayTrips</span>
  </div>
  <div class="contact web">WWW.TIDEWAYTRIPS.EXAMPLE</div>
</section>

<section class="card card-back">
  <div class="brand">
    <div class="brand-dot"></div>
    <div class="brand-name">Tideway Trips</div>
  </div>
</section>

</body>
</html>
```